Association Insurance WhitePaper

Need white paper layout design for cover page, data pages and back page, much like a powerpoint design. Looking for similar designs as the uploaded drawing style.

```html
<!DOCTYPE html>
<html lang="en">
<head>
<meta charset="utf-8">
<title>Harborline Cover — Association Insurance Whitepaper Layouts</title>
<link href="https://fonts.googleapis.com/css2?family=Plus+Jakarta+Sans:wght@400;500;600;700&display=swap" rel="stylesheet">
<style>
:root{
  --canvas:#c9d0d8;
  --navy:#435a7a;
  --navy-dark:#3a5173;
  --steel:#a3b0c2;
  --mist:#dadfe6;
  --panel:#eceff3;
  --ink:#4b505a;
  --white:#ffffff;
}
*{margin:0;padding:0;box-sizing:border-box}
html,body{width:1200px;height:1008px;overflow:hidden}
body{background:var(--canvas);font-family:"Plus Jakarta Sans",Arial,sans-serif;color:var(--ink);position:relative}
.slide{position:absolute;width:362px;height:203px;background:var(--white);overflow:hidden}
.abs{position:absolute}
.foot{position:absolute;left:0;right:0;bottom:0;height:5px;background:linear-gradient(90deg,var(--navy) 50%,var(--steel) 50%)}
.brand{position:absolute;left:18px;top:8px;display:flex;align-items:center;gap:2.5px}
.brand-mark{width:8px;height:8px;border:1px solid var(--navy);border-radius:1px}
.brand-name{font-size:4.4px;font-weight:600;color:var(--navy);text-transform:uppercase;letter-spacing:.2px;line-height:1}
.rule{position:absolute;left:64px;right:19px;top:12px;height:.5px;background:#e1e5ea}
.title{color:var(--navy-dark);font-weight:600;line-height:1.15;letter-spacing:-.2px}
.center{text-align:center;left:0;right:0}
.tiny{font-size:3.7px;line-height:1.55;color:var(--ink)}
.head-sm{font-size:7.4px;font-weight:600;color:var(--navy-dark)}
.photo{position:absolute}
/* agenda */
.agenda-pill{left:0;top:31px;width:111px;height:29px;background:var(--navy);border-radius:0 15px 15px 0;color:var(--white);font-size:18px;font-weight:600;padding-left:25px;line-height:29px}
.agenda-item{left:194px;width:140px}
.agenda-item .head-sm{font-size:7.6px;font-weight:500;margin-bottom:2px}
.agenda-item .tiny{padding-left:9px}
/* mission */
.mission-card{top:87px;width:97px;height:83px;background:var(--navy);color:var(--white);text-align:center;padding:12px 8px 0}
.mission-card svg{display:block;margin:0 auto}
.mission-card hr{border:0;height:.5px;background:rgba(255,255,255,.45);margin:6px 0 8px}
.mission-card h3{font-size:7.5px;font-weight:600;margin-bottom:2px}
.mission-card .tiny{color:#e3e8ef}
/* chart page */
.side-panel{left:0;top:54px;width:118px;height:120px;background:var(--panel)}
.side-item{left:21px;display:flex;gap:6px;width:92px}
.num{flex:none;width:7.5px;height:7.5px;background:var(--navy);color:var(--white);font-size:4.5px;font-weight:600;display:flex;align-items:center;justify-content:center;border-radius:1px;margin-top:1px}
.side-item .head-sm{font-size:6.8px;font-weight:500}
/* team */
.member{top:83px;width:59px;text-align:center}
.member-band{height:26px}
.avatar{position:absolute;left:13.5px;top:9px;width:32px;height:32px;border-radius:50%;border:2px solid var(--white)}
.member-name{margin-top:21px;font-size:7.4px;font-weight:500;color:var(--navy-dark)}
.member .tiny{font-size:3.3px}
/* hub */
.hub-icon{width:31px;height:31px;border-radius:50%;background:var(--navy);border:3px solid var(--white);box-shadow:0 0 3px rgba(60,80,110,.35);display:flex;align-items:center;justify-content:center}
.hub-label{font-size:5.6px;line-height:1.15;color:var(--navy-dark);text-align:center;width:40px}
/* bullets */
.bullet{left:36px;display:flex;gap:8px;width:120px}
.bullet-dot{flex:none;width:17px;height:17px;border-radius:50%;background:var(--navy);display:flex;align-items:center;justify-content:center}
.bullet .head-sm{font-size:6.2px;font-weight:500}
.bullet .tiny{font-size:3.4px}
.pct{font-size:10px;color:var(--navy);font-weight:500}
.legend{font-size:3.6px;color:var(--ink);display:flex;gap:8px;align-items:center}
.legend i{display:inline-block;width:3px;height:3px;margin-right:2px;vertical-align:middle}
/* contact */
.contact{left:192px;display:flex;gap:11px;align-items:flex-start;font-size:5.6px;line-height:1.3;color:#2f3440}
</style>
</head>
<body>

<!-- Cover -->
<section class="slide" style="left:39px;top:50px">
  <div class="photo" role="img" aria-label="Hand-drawn city skyline illustration with a harbour statue, watercolour wash in warm yellow behind blue ink buildings and water" style="left:0;top:36px;width:362px;height:167px;background:linear-gradient(180deg,#fdf8ee 0%,#fbe6b8 40%,#c3cedd 72%,#7b90ad 100%)"></div>
  <div class="abs" style="left:0;right:0;top:12px;display:flex;justify-content:center;align-items:center;gap:3px">
    <span class="brand-mark" style="width:13px;height:13px"></span>
    <span class="brand-name" style="font-size:6px">Harborline Cover</span>
  </div>
  <h1 class="abs center title" style="top:39px;font-size:19.5px;text-align:center;line-height:1.18">Community<br>Whitepaper<br>Headline Here</h1>
</section>

<!-- Agenda -->
<section class="slide" style="left:419px;top:50px">
  <div class="abs agenda-pill">Agenda</div>
  <div class="photo" role="img" aria-label="Photo of a hand signing an insurance claim form on a clipboard" style="left:48px;top:69px;width:129px;height:106px;background:linear-gradient(135deg,#e9e9e7,#cfd1d3 60%,#b9a89a)"></div>
  <div class="abs agenda-item" style="top:56px"><div class="head-sm">1. Headline Here</div><p class="tiny">Lorem ipsum dolor sit amet dummy texts. Duis quis amet nunc vulputate dolor. Scelerisque ligula faucibus.</p></div>
  <div class="abs agenda-item" style="top:89px"><div class="head-sm">2. Headline Here</div><p class="tiny">Lorem ipsum dolor sit amet dummy texts. Duis quis amet nunc vulputate dolor. Scelerisque ligula faucibus.</p></div>
  <div class="abs agenda-item" style="top:122px"><div class="head-sm">3. Headline Here</div><p class="tiny">Lorem ipsum dolor sit amet dummy texts. Duis quis amet nunc vulputate dolor. Scelerisque ligula faucibus.</p></div>
  <div class="abs agenda-item" style="top:153px"><div class="head-sm">4. Headline Here</div><p class="tiny">Lorem ipsum dolor sit amet dummy texts. Duis quis amet nunc vulputate dolor. Scelerisque ligula faucibus.</p></div>
  <div class="foot"></div>
</section>

<!-- Mission -->
<section class="slide" style="left:798px;top:50px">
  <div class="brand"><span class="brand-mark"></span><span class="brand-name">Harborline Cover</span></div><div class="rule"></div>
  <h2 class="abs center title" style="top:36px;font-size:14px;text-align:center">Our Mission</h2>
  <p class="abs tiny" style="left:115px;width:132px;top:57px;text-align:center">Lorem ipsum dolor sit amet dummy texts. Duis quis amet nunc vulputate dolor. Scelerisque ligula faucibus.</p>
  <div class="abs mission-card" style="left:29px">
    <svg width="11" height="11" viewBox="0 0 12 12"><circle cx="6" cy="3.2" r="2.6" fill="#fff"/><path d="M1 12c0-3.3 2.2-5 5-5s5 1.7 5 5z" fill="#fff"/></svg>
    <hr><h3>Headline Here</h3><p class="tiny">Lorem ipsum dolor sit amet dummy texts. Duis quis amet nunc vulputate dolor scelerisque ligula</p>
  </div>
  <div class="abs mission-card" style="left:132.5px">
    <svg width="12" height="11" viewBox="0 0 12 12"><circle cx="3" cy="2.5" r="1.7" fill="#fff"/><circle cx="6" cy="2.5" r="1.7" fill="#fff"/><circle cx="9" cy="2.5" r="1.7" fill="#fff"/><rect x="1.5" y="5" width="9" height="2.5" rx="1" fill="#fff"/><path d="M1 9h7l3-1.5v2L8 12H1z" fill="#fff"/></svg>
    <hr><h3>Headline Here</h3><p class="tiny">Lorem ipsum dolor sit amet dummy texts. Duis quis amet nunc vulputate dolor scelerisque ligula</p>
  </div>
  <div class="abs mission-card" style="left:235px">
    <svg width="12" height="11" viewBox="0 0 12 12"><path d="M1 10l4-4 2 2 4-5" stroke="#fff" stroke-width="1.4" fill="none"/><path d="M8 2.5h3.2v3.2z" fill="#fff"/><rect x="1" y="10.5" width="10.5" height="1.2" fill="#fff"/></svg>
    <hr><h3>Headline Here</h3><p class="tiny">Lorem ipsum dolor sit amet dummy texts. Duis quis amet nunc vulputate dolor scelerisque ligula</p>
  </div>
  <div class="foot"></div>
</section>

<!-- Bar chart page -->
<section class="slide" style="left:39px;top:285px">
  <div class="brand"><span class="brand-mark"></span><span class="brand-name">Harborline Cover</span></div><div class="rule"></div>
  <h2 class="abs title" style="left:21px;top:29px;font-size:14px">Headline Goes Here</h2>
  <div class="abs side-panel"></div>
  <div class="abs side-item" style="top:67px"><span class="num">1</span><div><div class="head-sm">Headline Here</div><p class="tiny">Lorem ipsum dolor sit amet dummy texts. Duis quis amet nunc</p></div></div>
  <div class="abs side-item" style="top:105px"><span class="num">2</span><div><div class="head-sm">Headline Here</div><p class="tiny">Lorem ipsum dolor sit amet dummy texts. Duis quis amet nunc</p></div></div>
  <div class="abs side-item" style="top:142px"><span class="num">3</span><div><div class="head-sm">Headline Here</div><p class="tiny">Lorem ipsum dolor sit amet dummy texts. Duis quis amet nunc</p></div></div>
  <svg class="abs" style="left:0;top:0" width="362" height="203" viewBox="0 0 362 203" font-family="Plus Jakarta Sans, sans-serif" font-size="3.7" fill="#435a7a" text-anchor="middle">
    <line x1="130" y1="158.5" x2="343" y2="158.5" stroke="#d6dbe2" stroke-width=".5"/>
    <g>
      <rect x="141.7" y="73.3" width="5.5" height="84.7"/><rect x="153" y="110.7" width="5.5" height="47.3" fill="#a3b0c2"/><rect x="162" y="118.6" width="5.5" height="39.4" fill="#dadfe6"/>
      <rect x="195.4" y="108.7" width="5.5" height="49.3"/><rect x="206" y="71.3" width="5.5" height="86.7" fill="#a3b0c2"/><rect x="216" y="118.6" width="5.5" height="39.4" fill="#dadfe6"/>
      <rect x="249" y="89" width="5.5" height="69"/><rect x="260" y="122.5" width="5.5" height="35.5" fill="#a3b0c2"/><rect x="269.7" y="98.9" width="5.5" height="59.1" fill="#dadfe6"/>
      <rect x="302.8" y="69.4" width="5.5" height="88.6"/><rect x="313.7" y="102.8" width="5.5" height="55.2" fill="#a3b0c2"/><rect x="324" y="59.5" width="5.5" height="98.5" fill="#dadfe6"/>
    </g>
    <g>
      <text x="144.4" y="70">43%</text><text x="155.7" y="107.5">24%</text><text x="164.7" y="115.5">20%</text>
      <text x="198.1" y="105.5">25%</text><text x="208.7" y="68">44%</text><text x="218.7" y="115.5">20%</text>
      <text x="251.7" y="86">35%</text><text x="262.7" y="119.5">18%</text><text x="272.4" y="96">30%</text>
      <text x="305.5" y="66.5">45%</text><text x="316.4" y="99.5">28%</text><text x="326.7" y="56.5">50%</text>
    </g>
    <g text-anchor="start" fill="#4b505a" font-size="3.5">
      <rect x="199.5" y="166.8" width="2.6" height="2.6" fill="#435a7a"/><text x="204" y="169.3">Data 1</text>
      <rect x="225" y="166.8" width="2.6" height="2.6" fill="#a3b0c2"/><text x="229.5" y="169.3">Data 1</text>
      <rect x="250.5" y="166.8" width="2.6" height="2.6" fill="#dadfe6"/><text x="255" y="169.3">Data 1</text>
    </g>
  </svg>
  <div class="foot"></div>
</section>

<!-- Donut stats page -->
<section class="slide" style="left:419px;top:285px">
  <div class="brand"><span class="brand-mark"></span><span class="brand-name">Harborline Cover</span></div><div class="rule"></div>
  <h2 class="abs center title" style="top:30px;font-size:14px;text-align:center">Headline Goes Here</h2>
  <p class="abs tiny" style="left:115px;width:132px;top:51px;text-align:center">Lorem ipsum dolor sit amet dummy texts. Duis quis amet nunc vulputate dolor. Scelerisque ligula faucibus.</p>
  <svg class="abs" style="left:0;top:0" width="362" height="203" viewBox="0 0 362 203" font-family="Plus Jakarta Sans, sans-serif" font-size="10.5" font-weight="500" fill="#435a7a" text-anchor="middle">
    <g fill="none" stroke-width="5">
      <circle cx="87" cy="113.5" r="29" stroke="#eef0f3"/>
      <circle cx="87" cy="113.5" r="29" stroke="#435a7a" stroke-dasharray="109.3 200" transform="rotate(-90 87 113.5)"/>
      <circle cx="181" cy="113.5" r="29" stroke="#eef0f3"/>
      <circle cx="181" cy="113.5" r="29" stroke="#a3b0c2" stroke-dasharray="136.7 200" transform="rotate(-90 181 113.5)"/>
      <circle cx="276" cy="113.5" r="29" stroke="#eef0f3"/>
      <circle cx="276" cy="113.5" r="29" stroke="#dadfe6" stroke-dasharray="82 200" transform="rotate(-90 276 113.5)"/>
    </g>
    <text x="87" y="117.5">60%</text><text x="181" y="117.5">75%</text><text x="276" y="117.5">45%</text>
  </svg>
  <p class="abs tiny" style="left:52px;width:70px;top:158px;text-align:center">Lorem ipsum dolor sit amet dummy texts. Duis quis amet nunc vulputate dolor scelerisque ligula</p>
  <p class="abs tiny" style="left:146px;width:70px;top:158px;text-align:center">Lorem ipsum dolor sit amet dummy texts. Duis quis amet nunc vulputate dolor scelerisque ligula</p>
  <p class="abs tiny" style="left:241px;width:70px;top:158px;text-align:center">Lorem ipsum dolor sit amet dummy texts. Duis quis amet nunc vulputate dolor scelerisque ligula</p>
  <div class="foot"></div>
</section>

<!-- Timeline -->
<section class="slide" style="left:798px;top:285px">
  <div class="brand"><span class="brand-mark"></span><span class="brand-name">Harborline Cover</span></div><div class="rule"></div>
  <h2 class="abs center title" style="top:26px;font-size:14px;text-align:center">Timeline Area</h2>
  <svg class="abs" style="left:0;top:0" width="362" height="203" viewBox="0 0 362 203" font-family="Plus Jakarta Sans, sans-serif" text-anchor="middle">
    <line x1="51" y1="108.5" x2="311" y2="108.5" stroke="#a3b0c2" stroke-width=".6"/>
    <g fill="#435a7a"><circle cx="94" cy="108.5" r="1.2"/><circle cx="137" cy="108.5" r="1.2"/><circle cx="180.5" cy="108.5" r="1.2"/><circle cx="224" cy="108.5" r="1.2"/><circle cx="267" cy="108.5" r="1.2"/></g>
    <g>
      <circle cx="51" cy="107" r="20.5" fill="#a3b0c2"/>
      <circle cx="94" cy="73" r="20.5" fill="#435a7a"/>
      <circle cx="137" cy="143" r="20.5" fill="#435a7a"/>
      <circle cx="180.5" cy="73" r="20.5" fill="#a3b0c2"/>
      <circle cx="224" cy="143" r="20.5" fill="#435a7a"/>
      <circle cx="267" cy="73" r="20.5" fill="#435a7a"/>
      <circle cx="311" cy="107" r="20.5" fill="#a3b0c2"/>
    </g>
    <g fill="#fff" font-size="7" font-weight="600">
      <text x="51" y="105">2015</text><text x="94" y="71">2017</text><text x="137" y="141">2019</text><text x="180.5" y="71">2021</text><text x="224" y="141">2023</text><text x="267" y="71">2025</text><text x="311" y="105">2027</text>
    </g>
    <g fill="#eef1f5" font-size="3">
      <text x="51" y="110">Lorem ipsum</text><text x="51" y="114">dolor amet</text>
      <text x="94" y="76">Lorem ipsum</text><text x="94" y="80">dolor amet</text>
      <text x="137" y="146">Lorem ipsum</text><text x="137" y="150">dolor amet</text>
      <text x="180.5" y="76">Lorem ipsum</text><text x="180.5" y="80">dolor amet</text>
      <text x="224" y="146">Lorem ipsum</text><text x="224" y="150">dolor amet</text>
      <text x="267" y="76">Lorem ipsum</text><text x="267" y="80">dolor amet</text>
      <text x="311" y="110">Lorem ipsum</text><text x="311" y="114">dolor amet</text>
    </g>
  </svg>
  <div class="abs" style="left:21px;top:146px;width:72px"><div class="head-sm" style="font-size:7px">Headline Here</div><p class="tiny">Lorem ipsum dolor sit amet dummy texts. Duis quis amet nunc vulputate dolor scelerisque ligula</p></div>
  <div class="abs" style="left:268px;top:146px;width:72px;text-align:right"><div class="head-sm" style="font-size:7px">Headline Here</div><p class="tiny">Lorem ipsum dolor sit amet dummy texts. Duis quis amet nunc vulputate dolor scelerisque ligula</p></div>
  <div class="foot"></div>
</section>

<!-- Workflow -->
<section class="slide" style="left:39px;top:519px">
  <div class="brand"><span class="brand-mark"></span><span class="brand-name">Harborline Cover</span></div><div class="rule"></div>
  <h2 class="abs center title" style="top:35px;font-size:14px;text-align:center">Workflow Area</h2>
  <p class="abs tiny" style="left:115px;width:132px;top:56px;text-align:center">Lorem ipsum dolor sit amet dummy texts. Duis quis amet nunc vulputate dolor. Scelerisque ligula faucibus.</p>
  <svg class="abs" style="left:0;top:0" width="362" height="203" viewBox="0 0 362 203" font-family="Plus Jakarta Sans, sans-serif" text-anchor="middle">
    <g fill="none" stroke-width="14">
      <path d="M33.2 123 A29.8 29.8 0 0 1 92.8 123" stroke="#435a7a"/>
      <path d="M92.8 123 A29.8 29.8 0 0 0 152.4 123" stroke="#a3b0c2"/>
      <path d="M152.4 123 A29.8 29.8 0 0 1 212 123" stroke="#435a7a"/>
      <path d="M212 123 A29.8 29.8 0 0 0 271.6 123" stroke="#a3b0c2"/>
      <path d="M271.6 123 A29.8 29.8 0 0 1 331.2 123" stroke="#435a7a"/>
    </g>
    <g font-size="4" font-weight="600">
      <circle cx="63" cy="114" r="5.5" fill="#435a7a"/><text x="63" y="115.5" fill="#fff">1</text>
      <circle cx="122.6" cy="130.5" r="5.5" fill="#a3b0c2"/><text x="122.6" y="132" fill="#fff">2</text>
      <circle cx="182.2" cy="114" r="5.5" fill="#435a7a"/><text x="182.2" y="115.5" fill="#fff">3</text>
      <circle cx="241.8" cy="130.5" r="5.5" fill="#a3b0c2"/><text x="241.8" y="132" fill="#fff">4</text>
      <circle cx="301.4" cy="114" r="5.5" fill="#435a7a"/><text x="301.4" y="115.5" fill="#fff">5</text>
    </g>
    <g font-size="6.2" fill="#3a5173" font-weight="500">
      <text x="63" y="130">Data 1</text><text x="122.6" y="93">Data 2</text><text x="182.2" y="130">Data 3</text><text x="241.8" y="93">Data 4</text><text x="301.4" y="130">Data 5</text>
    </g>
  </svg>
  <p class="abs tiny" style="left:41px;width:44px;top:133px;text-align:center;font-size:3.3px">Lorem ipsum dolor sit amet dummy texts. Duis quis amet nunc vulputate dolor scelerisque ligula.</p>
  <p class="abs tiny" style="left:100.6px;width:44px;top:96px;text-align:center;font-size:3.3px">Lorem ipsum dolor sit amet dummy texts. Duis quis amet nunc vulputate dolor scelerisque ligula.</p>
  <p class="abs tiny" style="left:160.2px;width:44px;top:133px;text-align:center;font-size:3.3px">Lorem ipsum dolor sit amet dummy texts. Duis quis amet nunc vulputate dolor scelerisque ligula.</p>
  <p class="abs tiny" style="left:219.8px;width:44px;top:96px;text-align:center;font-size:3.3px">Lorem ipsum dolor sit amet dummy texts. Duis quis amet nunc vulputate dolor scelerisque ligula.</p>
  <p class="abs tiny" style="left:279.4px;width:44px;top:133px;text-align:center;font-size:3.3px">Lorem ipsum dolor sit amet dummy texts. Duis quis amet nunc vulputate dolor scelerisque ligula.</p>
  <div class="foot"></div>
</section>

<!-- Team -->
<section class="slide" style="left:419px;top:519px">
  <div class="brand"><span class="brand-mark"></span><span class="brand-name">Harborline Cover</span></div><div class="rule"></div>
  <h2 class="abs center title" style="top:35px;font-size:14px;text-align:center">Team Headline</h2>
  <p class="abs tiny" style="left:115px;width:132px;top:56px;text-align:center">Lorem ipsum dolor sit amet dummy texts. Duis quis amet nunc vulputate dolor. Scelerisque ligula faucibus.</p>
  <div class="abs member" style="left:35px"><div class="member-band" style="background:var(--navy)"></div><div class="avatar" role="img" aria-label="Portrait photo of team member" style="background:linear-gradient(160deg,#d9c3b0,#8f7665)"></div><div class="member-name">Mara Ellison</div><p class="tiny">Lorem ipsum dolor sit amet dummy texts. Duis quis amet nunc vulputate dolor scelerisque ligula</p><p class="tiny" style="margin-top:5px">Ph: 123 456 7890<br>Em: mara@harborlinecover.com</p></div>
  <div class="abs member" style="left:112.5px"><div class="member-band" style="background:var(--steel)"></div><div class="avatar" role="img" aria-label="Portrait photo of team member" style="background:linear-gradient(160deg,#e7c9c4,#9c6e68)"></div><div class="member-name">Mara Ellison</div><p class="tiny">Lorem ipsum dolor sit amet dummy texts. Duis quis amet nunc vulputate dolor scelerisque ligula</p><p class="tiny" style="margin-top:5px">Ph: 123 456 7890<br>Em: mara@harborlinecover.com</p></div>
  <div class="abs member" style="left:191px"><div class="member-band" style="background:var(--navy)"></div><div class="avatar" role="img" aria-label="Portrait photo of team member" style="background:linear-gradient(160deg,#d5d0cb,#6f6660)"></div><div class="member-name">Mara Ellison</div><p class="tiny">Lorem ipsum dolor sit amet dummy texts. Duis quis amet nunc vulputate dolor scelerisque ligula</p><p class="tiny" style="margin-top:5px">Ph: 123 456 7890<br>Em: mara@harborlinecover.com</p></div>
  <div class="abs member" style="left:268.5px"><div class="member-band" style="background:var(--steel)"></div><div class="avatar" role="img" aria-label="Portrait photo of team member" style="background:linear-gradient(160deg,#e2d6cc,#7d6b5f)"></div><div class="member-name">Mara Ellison</div><p class="tiny">Lorem ipsum dolor sit amet dummy texts. Duis quis amet nunc vulputate dolor scelerisque ligula</p><p class="tiny" style="margin-top:5px">Ph: 123 456 7890<br>Em: mara@harborlinecover.com</p></div>
  <div class="foot"></div>
</section>

<!-- Coverage hub -->
<section class="slide" style="left:798px;top:519px">
  <div class="brand"><span class="brand-mark"></span><span class="brand-name">Harborline Cover</span></div><div class="rule"></div>
  <h2 class="abs center title" style="top:30px;font-size:14px;text-align:center">Headline Goes Here</h2>
  <svg class="abs" style="left:0;top:0" width="362" height="203" viewBox="0 0 362 203">
    <circle cx="180.5" cy="217.6" r="89.6" fill="none" stroke="#a3b0c2" stroke-width=".6" stroke-dasharray="1.5 1.5"/>
    <circle cx="180.5" cy="216" r="70" fill="#435a7a"/>
    <g fill="#fff" stroke="#435a7a" stroke-width="1.3">
      <circle cx="97" cy="185" r="2.6"/><circle cx="128.5" cy="145" r="2.6"/><circle cx="180.5" cy="128" r="2.6"/><circle cx="232.5" cy="145" r="2.6"/><circle cx="264" cy="185" r="2.6"/>
    </g>
  </svg>
  <div class="abs" style="left:0;right:0;top:170px;text-align:center;color:#fff;font-size:11.5px;font-weight:600;line-height:1.1">Headline<br>Goes Here</div>
  <div class="abs hub-label" style="left:160.5px;top:58px">Headline<br>Goes Here</div>
  <div class="abs hub-label" style="left:92.5px;top:79px">Headline<br>Goes Here</div>
  <div class="abs hub-label" style="left:229px;top:79px">Headline<br>Goes Here</div>
  <div class="abs hub-label" style="left:44px;top:129px">Headline<br>Goes Here</div>
  <div class="abs hub-label" style="left:277.5px;top:129px">Headline<br>Goes Here</div>
  <div class="abs hub-icon" style="left:165px;top:77px"><svg width="11" height="11" viewBox="0 0 12 12"><path d="M6 1L1 5.5h1.5V11h7V5.5H11z" fill="#fff"/></svg></div>
  <div class="abs hub-icon" style="left:97px;top:97.5px"><svg width="11" height="11" viewBox="0 0 12 12"><path d="M2 7l1.3-3h5.4L10 7v3H2z" fill="#fff"/><circle cx="4" cy="8" r=".9" fill="#435a7a"/><circle cx="8" cy="8" r=".9" fill="#435a7a"/></svg></div>
  <div class="abs hub-icon" style="left:233.5px;top:97.5px"><svg width="11" height="11" viewBox="0 0 12 12"><path d="M6 10.5L1.5 6A2.6 2.6 0 016 2.8 2.6 2.6 0 0110.5 6z" fill="#fff"/></svg></div>
  <div class="abs hub-icon" style="left:48.5px;top:147.5px"><svg width="11" height="11" viewBox="0 0 12 12"><path d="M6 1l4.5 1.8V6c0 2.7-2 4.4-4.5 5-2.5-.6-4.5-2.3-4.5-5V2.8z" fill="#fff"/></svg></div>
  <div class="abs hub-icon" style="left:282px;top:147.5px"><svg width="11" height="11" viewBox="0 0 12 12"><circle cx="6" cy="3.5" r="2.3" fill="#fff"/><path d="M1.5 11c0-2.8 2-4.3 4.5-4.3s4.5 1.5 4.5 4.3z" fill="#fff"/></svg></div>
</section>

<!-- Lawsuit protection article -->
<section class="slide" style="left:39px;top:754px">
  <div class="brand"><span class="brand-mark"></span><span class="brand-name">Harborline Cover</span></div><div class="rule"></div>
  <div class="photo" role="img" aria-label="Photo of paper family figures sheltered under a paper umbrella held in a hand" style="left:0;top:26px;width:78px;height:76px;background:linear-gradient(160deg,#6f8a56,#a7b48c 55%,#e6e1d6)"></div>
  <div class="photo" role="img" aria-label="Photo of a hand holding an umbrella over a small model house" style="left:78px;top:26px;width:79px;height:76px;background:linear-gradient(160deg,#b9b2a8,#e7e3dc 50%,#8c7f72)"></div>
  <h2 class="abs title" style="left:166px;top:34px;font-size:13.5px;line-height:1.12">Protecting the<br>Association from<br>Lawsuits</h2>
  <p class="abs tiny" style="left:166px;top:81px;width:150px">Lorem ipsum dolor sit amet dummy texts. Duis quis amet nunc vulputate dolor. Scelerisque ligula faucibus.</p>
  <div class="abs" style="left:15px;top:118px;width:58px"><div class="head-sm" style="font-size:6px;font-weight:500;line-height:1.3">Key Coverages Every Association Needs</div><p class="tiny" style="margin-top:7px;font-size:3.4px">Lorem ipsum dolor sit amet dummy texts. Duis quis amet nunc vulputate dolor. Scelerisque ligula velit nulla faucibus donec pellentesque massa mi. Aliquam in fusce semper aliquam egestas.</p></div>
  <div class="abs" style="left:82px;top:118px;width:58px"><div class="head-sm" style="font-size:6px;font-weight:500;line-height:1.3">Protecting Common Areas and Structures</div><p class="tiny" style="margin-top:7px;font-size:3.4px">Lorem ipsum dolor sit amet dummy texts. Duis quis amet nunc vulputate dolor. Scelerisque ligula velit nulla faucibus donec pellentesque massa mi. Aliquam in fusce semper aliquam egestas.</p></div>
  <div class="photo" role="img" aria-label="Photo of an insurance agent shaking hands with a smiling couple at an office table" style="left:157px;top:102px;width:205px;height:101px;background:linear-gradient(120deg,#cdbfb2,#e8e2da 45%,#8e8a88)"></div>
</section>

<!-- Bullet & chart -->
<section class="slide" style="left:419px;top:754px">
  <div class="brand"><span class="brand-mark"></span><span class="brand-name">Harborline Cover</span></div><div class="rule"></div>
  <h2 class="abs center title" style="top:26px;font-size:14px;text-align:center">Bullet &amp; Chart Area</h2>
  <div class="abs bullet" style="top:67px"><span class="bullet-dot"><svg width="7" height="7" viewBox="0 0 8 8"><circle cx="3.3" cy="3.3" r="2.3" fill="none" stroke="#fff" stroke-width="1"/><path d="M5 5l2.2 2.2" stroke="#fff" stroke-width="1"/></svg></span><div><div class="head-sm">Headline Here</div><p class="tiny">Lorem ipsum dolor sit amet dummy texts. Duis quis amet nunc vulputate dolor scelerisque ligula.</p></div></div>
  <div class="abs bullet" style="top:96.5px"><span class="bullet-dot" style="background:var(--steel)"><svg width="7" height="7" viewBox="0 0 8 8"><circle cx="4" cy="2.4" r="1.7" fill="#fff"/><path d="M1 8c0-2.2 1.3-3.3 3-3.3S7 5.8 7 8z" fill="#fff"/></svg></span><div><div class="head-sm">Headline Here</div><p class="tiny">Lorem ipsum dolor sit amet dummy texts. Duis quis amet nunc vulputate dolor scelerisque ligula.</p></div></div>
  <div class="abs bullet" style="top:126.5px"><span class="bullet-dot"><svg width="7" height="7" viewBox="0 0 8 8"><path d="M7.5.5L.5 3.6l3 1 1 3z" fill="#fff"/></svg></span><div><div class="head-sm">Headline Here</div><p class="tiny">Lorem ipsum dolor sit amet dummy texts. Duis quis amet nunc vulputate dolor scelerisque ligula.</p></div></div>
  <div class="abs bullet" style="top:157.5px"><span class="bullet-dot" style="background:var(--steel)"><svg width="7" height="7" viewBox="0 0 8 8"><path d="M.5 7l2.5-3.5 1.8 2L6 4l1.5 3z" fill="#fff"/><circle cx="5.8" cy="1.8" r=".9" fill="#fff"/></svg></span><div><div class="head-sm">Headline Here</div><p class="tiny">Lorem ipsum dolor sit amet dummy texts. Duis quis amet nunc vulputate dolor scelerisque ligula.</p></div></div>
  <svg class="abs" style="left:0;top:0" width="362" height="203" viewBox="0 0 362 203">
    <g fill="none" stroke-width="14" transform="rotate(-90 263 120)">
      <circle cx="263" cy="120" r="37.5" stroke="#435a7a" stroke-dasharray="129.6 300"/>
      <circle cx="263" cy="120" r="37.5" stroke="#a3b0c2" stroke-dasharray="54.2 300" stroke-dashoffset="-129.6"/>
      <circle cx="263" cy="120" r="37.5" stroke="#c6cdd7" stroke-dasharray="30.6 300" stroke-dashoffset="-183.8"/>
      <circle cx="263" cy="120" r="37.5" stroke="#e1e4e8" stroke-dasharray="21.2 300" stroke-dashoffset="-214.4"/>
    </g>
    <g fill="#435a7a"><rect x="255" y="121" width="2.6" height="6"/><rect x="259" y="117" width="2.6" height="10"/><rect x="263" y="119" width="2.6" height="8"/><rect x="267" y="114" width="2.6" height="13"/><rect x="253.5" y="127.5" width="17.5" height="1"/></g>
    <path d="M254.5 117l4.5-4 3.5 2.5 6-5.5" fill="none" stroke="#435a7a" stroke-width="1"/>
  </svg>
  <div class="abs pct" style="left:229px;top:60px">10%</div>
  <div class="abs pct" style="left:196px;top:89px">15%</div>
  <div class="abs pct" style="left:195px;top:139px">25%</div>
  <div class="abs pct" style="left:312px;top:113px">60%</div>
  <div class="abs legend" style="left:224px;top:174px"><span><i style="background:var(--navy)"></i>Data</span><span><i style="background:var(--steel)"></i>Data</span><span><i style="background:#c6cdd7"></i>Data</span><span><i style="background:#e1e4e8"></i>Data</span></div>
  <div class="foot"></div>
</section>

<!-- Thank you -->
<section class="slide" style="left:798px;top:754px">
  <div class="photo" role="img" aria-label="Photo of a young couple on a sofa shaking hands with an insurance advisor" style="left:0;top:30px;width:170px;height:144px;background:linear-gradient(130deg,#ddd6cc,#c9bcae 45%,#6d6664 85%)"></div>
  <div class="abs" style="left:188.5px;top:40px;display:flex;align-items:center;gap:3px"><span class="brand-mark" style="width:12px;height:12px"></span><span class="brand-name" style="font-size:5.6px">Harborline Cover</span></div>
  <h2 class="abs title" style="left:188.5px;top:70px;font-size:17px">Thank you</h2>
  <div class="abs contact" style="top:101px"><svg width="6" height="6" viewBox="0 0 8 8"><path d="M1.2.5h1.8l.8 2-1.1.8a5 5 0 002 2l.8-1.1 2 .8v1.8c0 .4-.3.7-.7.7A6.9 6.9 0 01.5 1.2c0-.4.3-.7.7-.7z" fill="#435a7a"/></svg><span>+123 456 7890<br>+123 456 7890</span></div>
  <div class="abs contact" style="top:123px"><svg width="6" height="6" viewBox="0 0 8 8"><path d="M7.5.5L.5 3.6l3 1 1 3z" fill="#435a7a"/></svg><span>info@harborlinecover.com<br>www.harborlinecover.com</span></div>
  <div class="abs contact" style="top:143px"><svg width="6" height="6" viewBox="0 0 8 8"><path d="M4 .6L.4 4h1.1v3.5h5V4h1.1z" fill="#435a7a"/></svg><span>1234 Street name, town/city<br>State/Country, Post 1234</span></div>
</section>

</body>
</html>
```